Media Company's Events Website Needs a Design

International Media Company is setting up a new website to market own and partners' events in the Asia Pacific region.

The sitemap and sections are described in the attached document. Supporting images, logos and layout for the mockups are also provided.

We require design mockups for 4 key pages. Please submit homepage mockup for evaluation first. We will give the go-ahead for the other 3 pages once your homepage design is approved, so you do not have to waste unnecessary time.

Any question which I did not cover, please email milo+artpanel@brightvane.example. Thanks!
Updates

Hi all designers, our client has decided to simplify the website, dropping 2 event categories and focusing on just 1 (i.e. Vivid Pathways). 

I am uploading a new homepage layout doc. 

Specifically, changes are:
- New set of tabs on the main menu
- Content area will include: (i) testimonial slider; (ii) video block; (iii) list of upcoming events. feel free to play around with the layout.

Thanks and sorry for the trouble!
Milo

Hi all designers, I have re-uploaded the new brief with respect to the section changes.

Please download and refer to the changes.

Thanks!

Target Market(s)

Corporations, Businessmen, C-level Executives

Industry/Entity Type

Events

Requirements
Must have
• Refer to layout document
Nice to have
• The website may be implemented using WordPress, so a typical 1- and 2-column layout would be deployment-friendly.

```html
<!DOCTYPE html>
<html lang="en">
<head>
<meta charset="utf-8">
<title>Vivid Pathways — Home</title>
<link rel="stylesheet" href="https://fonts.googleapis.com/css2?family=Arimo:wght@400;700&family=Open+Sans:ital,wght@0,400;0,600;0,700;1,400;1,700;1,800&family=Roboto+Condensed:wght@700&family=Ubuntu:wght@400;500;700&display=swap">
<style>
:root{
  --navy:#1d4466;
  --nav-top:#2f6185;
  --nav-bot:#173a57;
  --orange:#e8801f;
  --orange-dark:#c9620d;
  --link-blue:#1a5d8e;
  --title-blue:#1d4f7c;
  --text:#4a4a4a;
  --muted:#888;
  --footer-text:#d6d6d6;
  --photo-warm:#b3773c;
  --photo-dark:#3a2a1e;
}
*{box-sizing:border-box;margin:0;padding:0}
html,body{width:960px;height:1200px;overflow:hidden;background:#fff}
body{font-family:"Open Sans",Arial,sans-serif;color:var(--text)}
.canvas{position:relative;width:960px;height:1200px;overflow:hidden;background:#fff}
.abs{position:absolute}

/* header */
.header{position:absolute;left:0;top:0;width:960px;height:102px;background:linear-gradient(#fff,#f1f1f1);border-top:2px solid #555}
.brand{position:absolute;left:84px;top:30px;font-family:Arimo,Arial,sans-serif;font-size:35px;color:#555;letter-spacing:-1.5px}
.brand-sub{position:absolute;left:270px;top:64px;font-family:Arimo,Arial,sans-serif;font-size:10px;font-weight:700;color:#aaa}
.top-btn{position:absolute;top:10px;height:18px;border-radius:4px;font:11px Arimo,Arial,sans-serif;text-align:center;line-height:18px;color:#444;background:linear-gradient(#f3f3f3,#cfcfcf);box-shadow:0 1px 1px rgba(0,0,0,.25)}
.top-btn.primary{background:linear-gradient(#2f5a7e,#183a57);color:#fff}
.search{position:absolute;left:703px;top:56px;width:176px;height:24px;border:1px solid #ddd;border-radius:12px;background:#fff;font:10px Arimo,Arial,sans-serif;color:#aaa;padding:6px 10px}
.search svg{position:absolute;right:6px;top:4px}

/* nav */
.nav{position:absolute;left:0;top:102px;width:960px;height:31px;background:linear-gradient(var(--nav-top),var(--nav-bot))}
.nav a{position:absolute;top:0;color:#fff;font:11px Arimo,Arial,sans-serif;line-height:31px;text-decoration:none;transform:translateX(-50%);white-space:nowrap}
.nav .sep{position:absolute;top:4px;width:1px;height:24px;background:rgba(255,255,255,.18)}
.nav-home{position:absolute;left:88px;top:96px;width:76px;height:44px;border-radius:5px;background:linear-gradient(#f6a24a,var(--orange-dark));color:#fff;font:11px Arimo,Arial,sans-serif;text-align:center;line-height:42px}

/* hero */
.hero-frame{position:absolute;left:81px;top:150px;width:798px;height:278px;border:1px solid #e3e3e3;background:#fff}
.hero{position:absolute;left:90px;top:159px;width:780px;height:268px}
.hero-text{position:absolute;color:#fff}
.hero-make{left:12px;top:4px;font:italic 800 48px "Open Sans",sans-serif;letter-spacing:1px}
.hero-biz{left:150px;top:26px;font:italic 700 24px "Open Sans",sans-serif}
.hero-boom{left:12px;top:64px;font:italic 700 22px "Open Sans",sans-serif}
.hero-quote{left:12px;top:104px;width:290px;font-size:10.5px;line-height:16px}
.hero-author{left:12px;top:176px;font:italic 700 10px "Open Sans",sans-serif;line-height:16px;text-decoration:underline}
.read-more{position:absolute;left:12px;top:223px;width:111px;height:28px;border-radius:8px;background:linear-gradient(#fff,#dcdcdc);box-shadow:0 1px 3px rgba(0,0,0,.4);font:600 12px "Open Sans",sans-serif;color:#333;line-height:28px;padding-left:32px;letter-spacing:.5px}
.read-more svg{position:absolute;left:11px;top:7px}
.dots{position:absolute;left:198px;top:245px;display:flex;gap:6px}
.dots span{width:13px;height:13px;border-radius:50%;background:#fff;box-shadow:0 1px 2px rgba(0,0,0,.4)}
.dots span.on{background:#333;border:2px solid #fff}

/* about */
.about{position:absolute;left:88px;top:455px;width:534px;height:220px;border-radius:14px;background:linear-gradient(135deg,#fff 40%,#ececec)}
.section-title{position:absolute;font:500 17px Ubuntu,sans-serif;color:#222;white-space:nowrap}
.section-title b{font-weight:700;color:var(--title-blue)}
.section-title .accent{color:var(--link-blue);font-weight:400}
.rule{position:absolute;height:0;border-top:1px dotted #aaa}
.photo{position:absolute;background:linear-gradient(135deg,var(--photo-warm),var(--photo-dark))}
.photo-frame{position:absolute;background:#fff;border:1px solid #e2e2e2;box-shadow:0 1px 2px rgba(0,0,0,.1)}
.about-copy{position:absolute;left:290px;top:510px;width:327px;font-size:9.3px;line-height:14.4px;color:var(--text);text-align:justify}
.about-copy .lead{color:var(--orange)}
.about-copy p+p{margin-top:14px}
.shadow-bar{position:absolute;height:10px;border-radius:50%;background:radial-gradient(ellipse at center,rgba(0,0,0,.28),rgba(0,0,0,0) 70%)}

/* video */
.video{position:absolute;left:642px;top:484px;width:234px;height:160px;background:linear-gradient(135deg,#8a6040,#2b2b2b)}
.video-title{position:absolute;left:0;top:0;width:234px;height:11px;background:#111;color:#fff;font:bold 6px Arimo,Arial,sans-serif;padding:2px 20px}
.video-bar{position:absolute;left:0;bottom:0;width:234px;height:20px;background:linear-gradient(#444,#111);color:#ddd;font:5.5px Arimo,Arial,sans-serif;padding:2px 3px;line-height:8px}
.small-btn{position:absolute;top:663px;height:18px;border:1px solid #ccc;border-radius:2px;background:linear-gradient(#fff,#e8e8e8);font:bold 7px Arimo,Arial,sans-serif;color:#555;text-align:center;line-height:16px}
.dot-icon{position:absolute;border-radius:50%}

/* events */
.event{position:absolute;width:250px;height:64px}
.event .photo-frame{left:0;top:0;width:85px;height:60px}
.event .photo{left:4px;top:4px;width:76px;height:50px}
.event-date{position:absolute;left:92px;top:1px;font:700 10px Arimo,Arial,sans-serif;color:var(--title-blue)}
.event-desc{position:absolute;left:92px;top:15px;width:130px;font-size:8.5px;line-height:11.2px;color:#333}
.event-loc{position:absolute;left:92px;top:39px;font:10px Arimo,Arial,sans-serif;color:var(--link-blue)}

/* testimonials */
.testimonial{position:absolute;left:643px;width:236px;height:60px}
.testimonial .photo-frame{left:0;top:0;width:80px;height:56px}
.testimonial .photo{left:3px;top:3px;width:74px;height:50px;background:linear-gradient(135deg,#4a6a86,#20364a)}
.t-text{position:absolute;left:91px;top:0;width:143px;font-size:8.6px;line-height:12.8px;color:#333;letter-spacing:.2px}
.t-text b{font-weight:700}
.t-name{position:absolute;right:2px;top:45px;font:italic 8.5px Arimo,Arial,sans-serif;color:var(--link-blue);text-decoration:underline}

/* footer */
.band{position:absolute;left:0;top:1007px;width:960px;height:32px;background:linear-gradient(#3a3a3a,#272727)}
.band-label{position:absolute;left:103px;top:9px;font:700 11px "Roboto Condensed",Arial,sans-serif;color:#fff;white-space:nowrap}
.band-input{position:absolute;top:8px;height:17px;background:#fafafa;border:1px solid #aaa;font:italic 8px Arimo,Arial,sans-serif;color:#888;padding:3px 5px}
.band-btn{position:absolute;left:452px;top:8px;width:59px;height:17px;background:linear-gradient(#f1f1f1,#bdbdbd);border:1px solid #777;font:bold 9px Arimo,Arial,sans-serif;color:#333;text-align:center;line-height:15px}
.band-links{position:absolute;right:83px;top:10px;font:10px Arimo,Arial,sans-serif;color:#bbb;white-space:nowrap}
.band-links span{margin:0 4px;color:#888}
.footer{position:absolute;left:0;top:1039px;width:960px;height:161px;background:linear-gradient(#262626,#1a1a1a)}
.foot-title{position:absolute;font:700 18px Ubuntu,sans-serif;color:#fff;white-space:nowrap}
.foot-title span{color:#4d9fd6}
.foot-list{position:absolute;list-style:none;font-size:10px;line-height:19.2px;color:var(--footer-text);white-space:nowrap}
.foot-list li::before{content:"";display:inline-block;width:0;height:0;border-left:4px solid #ddd;border-top:3px solid transparent;border-bottom:3px solid transparent;margin-right:10px;vertical-align:1px}
.badge{position:absolute;border-radius:3px}
.contact{position:absolute;left:677px;top:1085px;width:200px;font-size:10px;color:#eee;line-height:17.6px}
.contact .mail{display:block;color:#4d9fd6;font-weight:700}
.contact-row{position:relative;height:17.6px;white-space:nowrap}
.contact-row .value{position:absolute;left:58px;top:0}
.contact-row .value.wide{left:87px}
</style>
</head>
<body>
<div class="canvas">

  <header class="header">
    <div class="brand">Vivid Pathways</div>
    <svg class="abs" style="left:327px;top:24px" width="20" height="20" viewBox="0 0 20 20" aria-hidden="true"><circle cx="10" cy="10" r="8" fill="#e8801f"/></svg>
    <div class="brand-sub">@ NORTHWAVE</div>
    <div class="top-btn primary" style="left:691px;width:46px">Login</div>
    <div class="top-btn" style="left:745px;width:56px">Register</div>
    <div class="top-btn" style="left:808px;width:67px">Newsletter</div>
    <div class="search">Search Here
      <svg width="20" height="16" viewBox="0 0 20 16" aria-hidden="true"><circle cx="8" cy="7" r="5.5" fill="none" stroke="#e8801f" stroke-width="2"/><line x1="12" y1="11" x2="17" y2="15" stroke="#e8801f" stroke-width="2.5"/></svg>
    </div>
  </header>

  <nav class="nav">
    <span class="sep" style="left:171px"></span>
    <a style="left:261px">About Vivid Pathways</a>
    <span class="sep" style="left:340px"></span>
    <a style="left:420px">Upcoming Events</a>
    <span class="sep" style="left:493px"></span>
    <a style="left:550px">Past Events</a>
    <span class="sep" style="left:613px"></span>
    <a style="left:660px">Videos</a>
    <span class="sep" style="left:718px"></span>
    <a style="left:814px">Partnership Opportunities</a>
  </nav>
  <div class="nav-home">Home</div>

  <div class="hero-frame"></div>
  <section class="hero">
    <svg class="abs" style="left:0;top:0" width="780" height="268" viewBox="0 0 780 268">
      <defs>
        <linearGradient id="blue" x1="0" y1="0" x2="1" y2="1"><stop offset="0" stop-color="#4c7593"/><stop offset="1" stop-color="#1f4562"/></linearGradient>
        <linearGradient id="hall" x1="0" y1="0" x2="0" y2="1"><stop offset="0" stop-color="#8a7a63"/><stop offset=".45" stop-color="#5c4c3c"/><stop offset="1" stop-color="#2d2a2a"/></linearGradient>
      </defs>
      <rect x="0" y="0" width="780" height="268" fill="url(#hall)" role="img" aria-label="Photo of a conference banquet hall with seated delegates at round tables"/>
      <polygon points="0,0 376,0 298,190 350,268 0,268" fill="url(#blue)"/>
      <polyline points="376,0 298,190 350,268" fill="none" stroke="#fff" stroke-width="3"/>
    </svg>
    <div class="hero-text hero-make">Make</div>
    <div class="hero-text hero-biz">Your business</div>
    <div class="hero-text hero-boom">a booming one!</div>
    <p class="hero-text hero-quote">“What’s great about Hangzhou and having officials from the city come to San Francisco to share their ideas, we learn a lot about IP protection, about their real invest-ment in making it a really clean and global city”</p>
    <p class="hero-text hero-author">Daniel Marsh, Chief Commercial Officer,<br>Brightline Energy</p>
    <div class="read-more"><svg width="15" height="15" viewBox="0 0 15 15" aria-hidden="true"><circle cx="7.5" cy="7.5" r="7.5" fill="#222"/><path d="M6 4.5l3 3-3 3" fill="none" stroke="#fff" stroke-width="1.8"/></svg>READ MORE</div>
    <div class="dots"><span class="on"></span><span></span><span></span><span></span><span></span><span></span></div>
  </section>

  <section class="about"></section>
  <svg class="abs" style="left:104px;top:462px" width="60" height="32" viewBox="0 0 60 32" aria-hidden="true"><rect x="4" y="18" width="5" height="12" fill="#999"/><rect x="12" y="12" width="5" height="18" fill="#4a9a3a"/><rect x="20" y="8" width="5" height="22" fill="#2e6ea8"/><polyline points="4,24 16,14 26,20 52,4" fill="none" stroke="#d8262c" stroke-width="3"/><path d="M46 2l8 0-2 8z" fill="#d8262c"/></svg>
  <div class="section-title" style="left:166px;top:470px">About <span class="accent">Vivid</span> Pathways</div>
  <div class="rule" style="left:166px;top:501px;width:434px"></div>
  <div class="photo-frame" style="left:95px;top:512px;width:180px;height:122px"></div>
  <div class="photo" style="left:102px;top:518px;width:166px;height:110px" role="img" aria-label="Photo of executives in conversation at a cocktail table"></div>
  <div class="about-copy">
    <p><span class="lead">Northwave Asia’s newly formed “Vivid Pathways” team, based in Singa-pore, offers clients customized and integrated on air and on –ground turn – key 360</span> <b>solutions, tailored to client’s objectives,</b> allowing for closer integrated brand messaging. Providing bespoke events where specific topics and issues are discussed either with a panel of experts or in roundtables with other industry stakeholders.</p>
    <p>Co – branded between the client and Northwave Vivid Pathways, the whole look and feel of the event from beginning to end, concept and execution will be designed with the clients branding and messaging in mind.</p>
  </div>
  <div class="shadow-bar" style="left:100px;top:640px;width:170px"></div>
  <div class="shadow-bar" style="left:115px;top:676px;width:480px"></div>

  <svg class="abs" style="left:645px;top:454px" width="22" height="22" viewBox="0 0 22 22" aria-hidden="true"><rect x="5" y="5" width="12" height="12" transform="rotate(45 11 11)" fill="#2e6ea8" stroke="#9cc3e6" stroke-width="2"/></svg>
  <div class="section-title" style="left:674px;top:456px"><b style="color:#1b3f72">Latest</b>&nbsp; <b style="color:#222">Videos!</b></div>
  <div class="video" role="img" aria-label="Video still of a panel discussion on stage">
    <div class="video-title">Panel Highlights and Round Table Session</div>
    <svg class="abs" style="left:100px;top:59px" width="34" height="34" viewBox="0 0 34 34" aria-hidden="true"><circle cx="17" cy="17" r="15" fill="#111" stroke="#fff" stroke-width="2.5"/><path d="M13 10l11 7-11 7z" fill="#fff"/></svg>
    <div class="video-bar">▸ video options<br>▸ playlist (1)</div>
  </div>
  <div class="small-btn" style="left:703px;width:36px">Embed</div>
  <div class="small-btn" style="left:741px;width:30px">Email</div>
  <div class="abs" style="left:779px;top:660px;width:1px;height:36px;background:#ddd"></div>
  <div class="dot-icon" style="left:795px;top:662px;width:20px;height:20px;background:#3b5b9a"></div>
  <div class="dot-icon" style="left:819px;top:662px;width:20px;height:20px;background:#c8338f"></div>
  <div class="dot-icon" style="left:843px;top:662px;width:20px;height:20px;background:#d6412f"></div>
  <div class="abs" style="left:795px;top:684px;font:6px Arimo,Arial,sans-serif;color:#777">More ▾</div>
  <div class="abs" style="left:807px;top:697px;width:60px;height:14px;background:#d6412f;border-radius:2px;color:#fff;font:bold 7px Arimo,Arial,sans-serif;text-align:center;line-height:14px">Hangout</div>

  <svg class="abs" style="left:84px;top:706px" width="32" height="30" viewBox="0 0 32 30" aria-hidden="true"><rect x="2" y="2" width="22" height="22" rx="4" fill="#f08a1c"/><path d="M7 19a2 2 0 1 0 .1 0M7 13a6 6 0 0 1 6 6M7 8a11 11 0 0 1 11 11" fill="none" stroke="#fff" stroke-width="2"/><ellipse cx="14" cy="26" rx="12" ry="3" fill="none" stroke="#222" stroke-width="1.5"/></svg>
  <div class="section-title" style="left:125px;top:710px"><b>Upcoming</b> Events</div>
  <div class="rule" style="left:125px;top:743px;width:469px"></div>

  <div class="event" style="left:90px;top:757px"><div class="photo-frame"></div><div class="photo" role="img" aria-label="Event photo"></div><div class="event-date">September 12 2012</div><div class="event-desc">Lorem Ipsum is simply dummy text of the printing</div><div class="event-loc">Tianjin, China</div></div>
  <div class="event" style="left:354px;top:757px"><div class="photo-frame"></div><div class="photo" role="img" aria-label="Event photo"></div><div class="event-date">September 12 2012</div><div class="event-desc">Lorem Ipsum is simply dummy text of the printing</div><div class="event-loc">Tianjin, China</div></div>
  <div class="event" style="left:90px;top:830px"><div class="photo-frame"></div><div class="photo" role="img" aria-label="Event photo"></div><div class="event-date">September 12 2012</div><div class="event-desc">Lorem Ipsum is simply dummy text of the printing</div><div class="event-loc">Tianjin, China</div></div>
  <div class="event" style="left:354px;top:830px"><div class="photo-frame"></div><div class="photo" role="img" aria-label="Event photo"></div><div class="event-date">September 12 2012</div><div class="event-desc">Lorem Ipsum is simply dummy text of the printing</div><div class="event-loc">Tianjin, China</div></div>
  <div class="event" style="left:90px;top:901px"><div class="photo-frame"></div><div class="photo" role="img" aria-label="Event photo"></div><div class="event-date">September 12 2012</div><div class="event-desc">Lorem Ipsum is simply dummy text of the printing</div><div class="event-loc">Tianjin, China</div></div>
  <div class="event" style="left:354px;top:901px"><div class="photo-frame"></div><div class="photo" role="img" aria-label="Event photo"></div><div class="event-date">September 12 2012</div><div class="event-desc">Lorem Ipsum is simply dummy text of the printing</div><div class="event-loc">Tianjin, China</div></div>
  <div class="shadow-bar" style="left:90px;top:977px;width:450px"></div>

  <div class="abs" style="left:628px;top:712px;width:1px;height:280px;background:linear-gradient(#fff,#e4e4e4,#fff)"></div>
  <svg class="abs" style="left:650px;top:724px" width="40" height="34" viewBox="0 0 40 34" aria-hidden="true"><ellipse cx="20" cy="14" rx="16" ry="11" fill="#f08a1c"/><ellipse cx="15" cy="20" rx="12" ry="8" fill="#2e82c8"/><path d="M8 26l-3 6 9-4z" fill="#2e82c8"/></svg>
  <div class="section-title" style="left:694px;top:731px;color:#1b3f72;font-weight:700">Our Testimonials</div>

  <div class="testimonial" style="top:775px"><div class="photo-frame"></div><div class="photo" role="img" aria-label="Video still of an interviewee"></div><p class="t-text"><b>They are really the</b> conduit for new technologies and applica-tions and they're doing a lot,</p><div class="t-name">Lee Carver, General Partner</div></div>
  <div class="testimonial" style="top:851px"><div class="photo-frame"></div><div class="photo" role="img" aria-label="Video still of an interviewee"></div><p class="t-text"><b>They are really the</b> conduit for new technologies and applica-tions and they're doing a lot,</p><div class="t-name">Lee Carver, General Partner</div></div>
  <div class="testimonial" style="top:926px"><div class="photo-frame"></div><div class="photo" role="img" aria-label="Video still of an interviewee"></div><p class="t-text"><b>They are really the</b> conduit for new technologies and applica-tions and they're doing a lot,</p><div class="t-name">Lee Carver, General Partner</div></div>

  <div class="band">
    <div class="band-label">News Letter Signup</div>
    <div class="band-input" style="left:196px;width:120px">Your Name</div>
    <div class="band-input" style="left:325px;width:120px">Your Email</div>
    <div class="band-btn">SUBCRIBE</div>
    <div class="band-links">Blog<span>|</span>Contact Us<span>|</span>Help<span>|</span>Terms of Service<span>|</span>Support<span>|</span>Privacy Policy</div>
  </div>

  <footer class="footer"></footer>
  <svg class="abs" style="left:95px;top:1045px" width="26" height="26" viewBox="0 0 26 26" aria-hidden="true"><circle cx="13" cy="13" r="11" fill="#4d9fd6"/><circle cx="13" cy="13" r="7" fill="#1f1f1f"/><circle cx="13" cy="13" r="4" fill="#fff"/></svg>
  <div class="foot-title" style="left:129px;top:1047px"><span>Links</span> &amp; Services</div>
  <ul class="foot-list" style="left:92px;top:1087px">
    <li>Login</li><li>Register</li><li>Newsletter Signup</li><li>Contact Us</li><li>Sitemap</li>
  </ul>
  <ul class="foot-list" style="left:218px;top:1087px">
    <li>Home</li><li>About Vivid Pathways</li><li>Upcoming Events</li><li>Past Events</li><li>Partnership Opportunities</li><li>Videos</li>
  </ul>
  <div class="badge" style="left:401px;top:1098px;width:86px;height:40px;background:#fff" role="img" aria-label="Partner event badge"></div>
  <div class="badge" style="left:500px;top:1102px;width:102px;height:33px;background:#f2f2f2;border:1px solid #bbb" role="img" aria-label="Partner event badge"></div>
  <div class="badge" style="left:407px;top:1147px;width:76px;height:44px;background:#1f3f88;border:1px solid #9ab" role="img" aria-label="Partner event badge"></div>
  <div class="badge" style="left:499px;top:1154px;width:100px;height:26px;background:#3d2f80;border:1px solid #ccc" role="img" aria-label="Partner event badge"></div>

  <svg class="abs" style="left:671px;top:1045px" width="30" height="28" viewBox="0 0 30 28" aria-hidden="true"><rect x="2" y="4" width="22" height="14" rx="3" fill="#4d9fd6"/><path d="M6 18l-2 8 8-8z" fill="#4d9fd6"/></svg>
  <div class="foot-title" style="left:712px;top:1047px"><span>Contact</span> info:</div>
  <div class="contact">
    <span class="mail">info@vividpathways.example</span>
    <div class="contact-row"><span>Phone:</span><span class="value">02 5550 1234</span></div>
    <div class="contact-row"><span>Mobile :</span><span class="value">0400 555 017</span></div>
    <div class="contact-row"><span>Office Hours :</span><span class="value wide">9:00am till 5:30pm</span></div>
  </div>
  <div class="dot-icon" style="left:677px;top:1168px;width:24px;height:24px;background:#c8241c"></div>
  <div class="dot-icon" style="left:709px;top:1168px;width:24px;height:24px;background:#3a6fb6"></div>
  <div class="dot-icon" style="left:742px;top:1168px;width:24px;height:24px;background:#3a8fd0"></div>
  <div class="dot-icon" style="left:775px;top:1168px;width:24px;height:24px;background:#2f5fa8"></div>

</div>
</body>
</html>
```